Business Card Design for a Personal Trainer

I need a business card design for my job as a personal trainer. It should have a unique, modern and exclusive design. On the front there should be only my logo with my name and my job. 0163/2918374 Tobias Kellinger Lindenfeldweg 14 80412 Munich Germany The most important contact information is the web adress. it can be bigger than the rest, but its not necessary. The card should be 8,5cmx5,5cm big. Font: Roboto. Colors: black, white, gray, 56c1ff.

```html
<!DOCTYPE html>
<html lang="de">
<head>
<meta charset="utf-8">
<title>Tobias Kellinger – Visitenkarte</title>
<link rel="stylesheet" href="https://fonts.googleapis.com/css2?family=Roboto:wght@300;400;500&display=swap">
<style>
  :root {
    --page-bg: #e9e7e4;
    --card-top: #2a2828;
    --card-bottom: #0d0c0c;
    --white: #f4f4f4;
    --gray: #9a9a9a;
    --accent: #56c1ff;
    --accent-dark: #2f8fcc;
  }
  * { box-sizing: border-box; margin: 0; padding: 0; }
  html, body {
    width: 1200px; height: 1200px; overflow: hidden;
    background: var(--page-bg);
    font-family: "Roboto", Arial, sans-serif;
  }
  .sheet {
    width: 1200px; height: 1200px;
    display: flex; flex-direction: column; align-items: center; justify-content: center;
    gap: 44px;
  }
  .card {
    position: relative;
    width: 800px; height: 518px;
    background: linear-gradient(135deg, var(--card-top), var(--card-bottom) 70%);
    border-radius: 6px;
    box-shadow: 0 14px 30px rgba(0,0,0,.25);
    overflow: hidden;
    color: var(--white);
  }
  /* front */
  .card-front { display: flex; align-items: center; justify-content: center; }
  .brand { text-align: center; }
  .brand-row { display: flex; align-items: center; gap: 22px; justify-content: center; }
  .brand-square { width: 54px; height: 54px; background: var(--white); }
  .brand-name { font-size: 54px; font-weight: 400; letter-spacing: 1px; }
  .brand-tagline {
    display: flex; align-items: center; gap: 14px; margin-top: 12px;
    color: var(--gray); font-size: 20px; font-weight: 300; letter-spacing: 8px;
  }
  .brand-tagline::before, .brand-tagline::after {
    content: ""; flex: 1; height: 2px; background: var(--gray);
  }
  /* back */
  .holder-name {
    position: absolute; left: 56px; top: 96px;
    font-size: 32px; font-weight: 400;
  }
  .portrait {
    position: absolute; left: 110px; top: 150px;
    width: 250px; height: 250px; border-radius: 50%;
    background: radial-gradient(circle at 50% 40%, var(--accent), var(--accent-dark));
  }
  .contacts {
    position: absolute; left: 440px; top: 80px;
    list-style: none; font-size: 22px; font-weight: 400; line-height: 1.3;
  }
  .contacts li { display: flex; align-items: flex-start; gap: 16px; margin-bottom: 34px; }
  .contacts svg { flex: none; width: 24px; height: 24px; margin-top: 2px; }
  .website-row {
    position: absolute; left: 0; right: 0; top: 412px;
    display: flex; align-items: center; gap: 18px;
  }
  .website-row .rule { height: 2px; background: var(--accent); }
  .rule-left { flex: 1; }
  .rule-right { width: 40px; }
  .website { font-size: 34px; font-weight: 400; white-space: nowrap; }
</style>
</head>
<body>
<main class="sheet">
  <section class="card card-front">
    <div class="brand">
      <div class="brand-row">
        <span class="brand-square"></span>
        <span class="brand-name">TOBIAS KELLINGER</span>
      </div>
      <div class="brand-tagline">PERSONAL TRAINER</div>
    </div>
  </section>

  <section class="card card-back">
    <h1 class="holder-name">Tobias Kellinger</h1>
    <div class="portrait" role="img" aria-label="Porträtfoto des Trainers auf blauem Kreis"></div>
    <ul class="contacts">
      <li>
        <svg viewBox="0 0 24 24"><path fill="var(--accent)" d="M6.6 10.8a15.1 15.1 0 0 0 6.6 6.6l2.2-2.2c.3-.3.7-.4 1-.2 1.1.4 2.3.6 3.6.6.6 0 1 .4 1 1V20c0 .6-.4 1-1 1A17 17 0 0 1 3 4c0-.6.4-1 1-1h3.5c.6 0 1 .4 1 1 0 1.3.2 2.5.6 3.6.1.3 0 .7-.2 1z"/></svg>
        <span>0163/2918374</span>
      </li>
      <li>
        <svg viewBox="0 0 24 24"><rect x="2" y="5" width="20" height="14" rx="1" fill="var(--accent)"/><path d="M3 6l9 7 9-7" fill="none" stroke="#1a1919" stroke-width="1.6"/></svg>
        <span>t.kellinger@postfeld.de</span>
      </li>
      <li>
        <svg viewBox="0 0 24 24"><path fill="var(--accent)" d="M12 2a7 7 0 0 0-7 7c0 5 7 13 7 13s7-8 7-13a7 7 0 0 0-7-7zm0 9.5A2.5 2.5 0 1 1 12 6.5a2.5 2.5 0 0 1 0 5z"/></svg>
        <span>Lindenfeldweg 14<br>80412 München</span>
      </li>
    </ul>
    <div class="website-row">
      <span class="rule rule-left"></span>
      <p class="website">www.tobiaskellinger.de</p>
      <span class="rule rule-right"></span>
    </div>
  </section>
</main>
</body>
</html>
```